Truck Parking Fyer Design

We need a flyer design for a new company based in Redland Bay called "Wattle Downs Truck Parking"
We have parking available for Tipper Trucks, Earthmoving Machinery & Shipping containers. Undercover area for Cars, Motorhomes, Caravans, Horse Floats and Boats. Rates are negotiable on length of time needed. eg. Truck and Dog = $50 per week + GST. 20 foot container $25 per week. Idea for local Redlands Residents. Owners are responsible for own insurance. We would like to see it as a simple design including different types of vehicles as mentioned above. with colours of earthmoving green (like grass) and brown like (dirt) - Lockup parking with owners living on site

```html
<!DOCTYPE html>
<html lang="en">
<head>
<meta charset="utf-8">
<title>Wattle Downs Truck Parking</title>
<link rel="stylesheet" href="https://fonts.googleapis.com/css2?family=Open+Sans:ital,wght@0,400;0,700;0,800;1,700&display=swap">
<style>
  :root {
    --sky-top: #1c8fd8;
    --sky-bottom: #cfe9f6;
    --dirt: #8b5a45;
    --grass: #a6cf3b;
    --leaf: #5aa63c;
    --forest: #17683f;
    --gold: #f5c51c;
    --ink: #1f2a24;
    --white: #ffffff;
  }
  * { box-sizing: border-box; margin: 0; padding: 0; }
  html, body { width: 854px; height: 1200px; overflow: hidden; background: #fff; }
  body { font-family: "Open Sans", Arial, sans-serif; }

  .flyer {
    position: relative;
    width: 854px;
    height: 1200px;
    overflow: hidden;
    background: var(--grass);
  }
  .sky {
    position: absolute; left: 0; top: 0; width: 854px; height: 518px;
    background: linear-gradient(180deg, var(--sky-top) 0%, #6fb8e6 40%, var(--sky-bottom) 100%);
  }
  .ground {
    position: absolute; left: 0; top: 518px; width: 854px; height: 177px;
    background: var(--dirt);
  }
  .brand {
    position: absolute; left: 0; top: 56px; width: 854px;
    text-align: center;
    color: var(--gold);
    font-weight: 800;
    font-size: 74px;
    line-height: 84px;
  }
  .headline {
    position: absolute; left: 0; top: 278px; width: 854px;
    text-align: center;
    color: var(--forest);
    font-weight: 700;
    font-size: 53px;
    line-height: 60px;
    letter-spacing: 0.5px;
  }
  .vehicles {
    position: absolute; left: 32px; top: 430px; width: 776px; height: 200px;
    background: linear-gradient(180deg, #f2f4f5 0%, #d9dde0 100%);
    border-radius: 6px;
    opacity: 0.92;
  }
  .rates {
    position: absolute; left: 64px; top: 660px; width: 730px; height: 78px;
    background: var(--leaf);
    color: var(--white);
    font-size: 29px;
    line-height: 78px;
    text-align: center;
  }
  .services {
    position: absolute; left: 0; width: 854px;
    text-align: center;
    color: var(--ink);
    font-size: 22px;
    line-height: 30px;
  }
  .services--trucks { top: 776px; }
  .services--undercover { top: 858px; }
  .services em { font-weight: 700; }
  .cta {
    position: absolute; left: 57px; top: 960px; width: 387px; height: 64px;
    background: var(--leaf);
    color: var(--white);
    font-weight: 700;
    font-size: 46px;
    line-height: 64px;
    text-align: center;
  }
  .contacts {
    position: absolute; left: 461px; top: 956px;
    color: var(--ink);
    font-weight: 700;
    font-size: 22px;
    line-height: 35px;
    list-style: none;
  }
  .address {
    position: absolute; left: 0; top: 1057px; width: 854px;
    text-align: center;
    color: var(--ink);
    font-weight: 700;
    font-size: 29px;
    line-height: 40px;
  }
  .footer {
    position: absolute; left: 0; top: 1125px; width: 854px; height: 75px;
    background: var(--dirt);
    color: var(--white);
    font-weight: 700;
    font-size: 22px;
    line-height: 75px;
    text-align: center;
  }
</style>
</head>
<body>
<main class="flyer">
  <div class="sky"></div>
  <div class="ground"></div>

  <h1 class="brand">Wattle Downs<br>Truck Parking</h1>

  <h2 class="headline">LOCK UP PARKING WITH<br>OWNERS LIVING ON SITE</h2>

  <div class="vehicles" role="img" aria-label="Line drawing of parked vehicles: motorhome, caravan, ute, another caravan and a boat on a trailer"></div>

  <p class="rates">Rates negotiable on length of time needed!</p>

  <p class="services services--trucks">Available for Tipper Trucks, Earthmoving<br>Machinery &amp; Shipping containers</p>
  <p class="services services--undercover"><em>Undercover area</em> for Cars, Motorhomes,<br>Caravans, Horse Floats and Boats</p>

  <p class="cta">Call us NOW</p>
  <ul class="contacts">
    <li>Danny mobile: 0412 555 018</li>
    <li>Maree mobile: 0402 555 274</li>
  </ul>

  <p class="address">27-31 Tallow Road, Kestrel Bay Qld 4199</p>

  <footer class="footer">Owners are responsible for own insurance</footer>
</main>
</body>
</html>
```